Business Cards

Need a neat design for a new business card

Industry/Entity Type

Residential Construction

Contact Information for Business Card

Company Name- KOVE Construction Inc.
Owner- Marcus Tolliver
Phone number- (555)203-7481
Email- kovecohomes@brindlemail.example
Facebook- www.socialpage.example/kovecohomes

Colors
fefdec

```html
<!DOCTYPE html>
<html lang="en">
<head>
<meta charset="utf-8">
<title>KOVE Construction Business Card</title>
<link href="https://fonts.googleapis.com/css2?family=Lato:wght@400;700;900&display=swap" rel="stylesheet">
<style>
  :root {
    --backdrop: #d6d6d6;
    --card-light: #ffffff;
    --card-dark: #07080a;
    --ink: #0d0d0d;
    --muted: #6f6f6f;
    --rule: #222222;
    --paper: #ffffff;
  }
  * { margin: 0; padding: 0; box-sizing: border-box; }
  html, body {
    width: 1200px;
    height: 1143px;
    overflow: hidden;
    background: var(--backdrop);
    font-family: "Lato", sans-serif;
  }
  .card {
    position: absolute;
    left: 299px;
    width: 602px;
    height: 343px;
  }
  .card--front { top: 180px; background: var(--card-light); }
  .card--back { top: 621px; background: var(--card-dark); }

  .wordmark {
    position: absolute;
    display: flex;
    flex-direction: column;
    align-items: center;
    font-family: "Lato", sans-serif;
    font-weight: 700;
    line-height: 1;
  }
  .wordmark__name { letter-spacing: 0.04em; }
  .wordmark__sub { letter-spacing: 0.16em; }

  .card--front .wordmark {
    left: 51px; top: 56px; width: 137px;
    color: var(--ink);
  }
  .card--front .wordmark__name { font-size: 44px; }
  .card--front .wordmark__sub { font-size: 11px; margin-top: 10px; }

  .card--back .wordmark {
    left: 0; right: 0; top: 104px;
    color: var(--paper);
  }
  .card--back .wordmark__name { font-size: 74px; }
  .card--back .wordmark__sub { font-size: 18px; margin-top: 16px; }

  .holder-name {
    position: absolute;
    right: 31px;
    top: 185px;
    font-size: 28px;
    font-weight: 900;
    color: var(--ink);
    letter-spacing: -0.01em;
  }
  .holder-rule {
    position: absolute;
    left: 31px;
    top: 231px;
    width: 478px;
    height: 1px;
    background: var(--rule);
  }
  .holder-role {
    position: absolute;
    right: 31px;
    top: 221px;
    font-size: 16px;
    color: var(--muted);
  }
  .contact-list {
    position: absolute;
    left: 31px;
    top: 244px;
    list-style: none;
  }
  .contact-list li {
    display: flex;
    align-items: center;
    height: 23px;
    font-size: 16px;
    color: var(--muted);
  }
  .contact-list svg {
    width: 17px;
    height: 17px;
    margin-right: 12px;
    flex: none;
  }
</style>
</head>
<body>
  <section class="card card--front">
    <div class="wordmark">
      <span class="wordmark__name">KOVE</span>
      <span class="wordmark__sub">CONSTRUCTION</span>
    </div>

    <div class="holder-name">Marcus Tolliver</div>
    <div class="holder-rule"></div>
    <div class="holder-role">Owner</div>

    <ul class="contact-list">
      <li>
        <svg viewBox="0 0 24 24" aria-hidden="true">
          <path d="M6.6 10.8a15.1 15.1 0 0 0 6.6 6.6l2.2-2.2a1 1 0 0 1 1-.25 11.4 11.4 0 0 0 3.6.57 1 1 0 0 1 1 1V20a1 1 0 0 1-1 1A17 17 0 0 1 3 4a1 1 0 0 1 1-1h3.5a1 1 0 0 1 1 1c0 1.25.2 2.45.57 3.6a1 1 0 0 1-.25 1z" fill="#0d0d0d"/>
          <path d="M14 3.5a6.5 6.5 0 0 1 6.5 6.5M14 7a3 3 0 0 1 3 3" stroke="#0d0d0d" stroke-width="1.8" fill="none" stroke-linecap="round"/>
        </svg>
        (555)203-7481
      </li>
      <li>
        <svg viewBox="0 0 24 24" aria-hidden="true">
          <rect x="2" y="5" width="20" height="14" fill="#0d0d0d"/>
          <path d="M2.5 5.5 12 13l9.5-7.5M2.5 18.5l7-6.5M21.5 18.5l-7-6.5" stroke="#ffffff" stroke-width="1.4" fill="none"/>
        </svg>
        kovecohomes@brindlemail.example
      </li>
      <li>
        <svg viewBox="0 0 24 24" aria-hidden="true">
          <circle cx="12" cy="12" r="10" stroke="#0d0d0d" stroke-width="2" fill="none"/>
        </svg>
        kovecohomes
      </li>
    </ul>
  </section>

  <section class="card card--back">
    <div class="wordmark">
      <span class="wordmark__name">KOVE</span>
      <span class="wordmark__sub">CONSTRUCTION</span>
    </div>
  </section>
</body>
</html>
```